Food broker, trader, wholesaler, liquidator looking for a 5 pages website

Looking for a 5 pages website design. We are food brokers, traders, wholesaler and closeout buyer working with manufacturers, distributors, importers sell to retailers, food service operators and industrial (ingredients). We help market their products. We are a resource for those who need a solution in the distribution/selling/placement of food on the shelves, kitchens and pantries. Whether we open new accounts with new products or sell short dated inventory, we know where to go and get results.

Target Market(s)

Food manufacturers, food distributors, food brokers

Coding

Coded - Design and coding required

Number of Pages Required

4 page

Font styles to use
Serif

Requirements
Must have
• Food-food production-warehouse-Food packaging-people meeting-trucks-supermarket shelves-

```html
<!DOCTYPE html>
<html lang="en">
<head>
<meta charset="utf-8">
<title>Harborline Provisions — Food &amp; Beverage Brokers</title>
<link href="https://fonts.googleapis.com/css2?family=Open+Sans:wght@400;600;700&family=Poppins:wght@600;700&display=swap" rel="stylesheet">
<style>
:root{
  --navy:#1b2470;
  --deep:#0f1766;
  --royal:#2f3aa0;
  --blue:#0b6fc7;
  --sky:#3aa8e8;
  --steel:#6a93cf;
  --indigo:#3f4aa3;
  --cyan:#33c6f0;
  --ink:#333;
  --mist:#e6e6ee;
  --panel:#ececee;
  --white:#fff;
}
*{margin:0;padding:0;box-sizing:border-box}
html,body{width:1200px;height:3555px;overflow:hidden;background:var(--white)}
body{position:relative;font-family:"Open Sans",sans-serif;color:var(--ink)}
h1,h2,h3{font-weight:inherit}
.abs{position:absolute}
/* header */
.site-header{left:0;top:0;width:1200px;height:59px;background:var(--white)}
.brand{left:248px;top:10px;display:flex;align-items:center;gap:10px;font-weight:700;font-size:17px;color:var(--navy);letter-spacing:.5px}
.brand-dot{width:36px;height:36px;border-radius:50%;background:var(--navy)}
.nav{left:625px;top:24px;display:flex;gap:25px;font-size:11.5px;font-weight:600;color:#333}
.phone{left:965px;top:18px;display:flex;align-items:center;gap:6px;font-size:17px;color:#222}
/* hero */
.hero-photo{left:0;top:59px;width:1200px;height:482px;background:linear-gradient(100deg,#6b5a35 0%,#b9a98a 25%,#d8d3c8 45%,#c9b08a 65%,#9c6b4a 85%,#b58f6b 100%)}
.hero-circle{left:64px;top:108px;width:380px;height:380px;border-radius:50%;background:var(--royal)}
.hero-title{left:120px;top:228px;font-family:"Poppins",sans-serif;font-weight:700;font-size:29px;line-height:33px;color:var(--white);white-space:nowrap}
.hero-title .accent{color:var(--cyan)}
.link-arrow{display:inline-flex;align-items:center;gap:8px}
.hero-link{left:124px;top:377px;font-size:11px;color:var(--cyan)}
/* intro */
.intro-panel{left:956px;top:541px;width:244px;height:604px;background:var(--panel)}
.intro-title{left:245px;top:656px;width:460px;font-weight:700;font-size:36.5px;line-height:42.5px;color:#333;letter-spacing:-.4px}
.intro-title .hl{color:var(--navy);background:linear-gradient(transparent 82%,#c8cbf0 82%)}
.btn-outline{border:2px solid #222;background:var(--white);font-size:12px;font-weight:700;color:#222;justify-content:center;white-space:nowrap}
.intro-btn{left:245px;top:947px;width:129px;height:35px}
.intro-bar{left:768px;top:648px;width:367px;height:33px;background:var(--blue)}
.intro-photo{left:714px;top:681px;width:450px;height:333px;background:linear-gradient(160deg,#1d2b4a 0%,#3c4a6a 40%,#8a8f99 70%,#b7b2a8 100%)}
/* features */
.feature-photo{left:181px;top:1200px;width:835px;height:470px;background:linear-gradient(90deg,#9a6a52 0%,#c9a99a 30%,#a8b4c4 60%,#c8ccd6 100%)}
.card{color:var(--white);text-align:center;padding:54px 22px 0}
.card h3{font-size:13px;font-weight:700;margin-bottom:10px}
.card p{font-size:10px;line-height:16px}
.card-service{left:426px;top:1120px;width:243px;height:190px;background:var(--steel)}
.card-quality{left:691px;top:1357px;width:243px;height:189px;background:var(--sky)}
.card-network{left:233px;top:1528px;width:243px;height:189px;background:var(--indigo)}
.icon-badge{width:94px;height:94px;border-radius:50%;background:var(--blue);display:flex;align-items:center;justify-content:center}
/* services */
.services-band{left:0;top:1797px;width:1200px;height:492px;background:var(--mist)}
.eyebrow{left:244px;top:1876px;font-size:14px;font-weight:700;color:#222}
.services-title{left:244px;top:1915px;width:500px;font-weight:700;font-size:28px;line-height:35px;color:var(--navy)}
.services-btn{left:787px;top:1944px;width:169px;height:46px;font-size:13px}
.service-tile{top:2091px;width:338px;height:365px}
.service-tile span{position:absolute;left:50px;bottom:62px;font-weight:700;font-size:31px;line-height:34px;color:var(--white);white-space:nowrap}
.tile-sales{left:80px;background:linear-gradient(150deg,#c7c2bd,#8f8c92 60%,#d9d6d2)}
.tile-trade{left:437px;background:linear-gradient(180deg,#5d6f86,#8d9bab 55%,#5b5a58)}
.tile-stock{left:789px;background:linear-gradient(160deg,#d0d3d8,#b49a8a 50%,#8c8e9a)}
/* retailers */
.trust-box{left:247px;top:2566px;width:710px;height:220px;border:3px solid #222}
.trust-title{left:327px;top:2549px;padding:0 14px;background:var(--white);font-weight:600;font-size:22px;color:#333;white-space:nowrap}
.retailer{width:76px;height:26px;border-radius:4px;background:#d6d9e3}
.retailer.tall{height:60px}
/* footer */
.footer-wave{left:0;top:2860px;width:1200px;height:626px}
.footer-brand{left:0;top:2967px;width:1200px;text-align:center;font-weight:700;font-size:18px;color:var(--white);letter-spacing:1px}
.cta-title{left:303px;top:3034px;font-weight:400;font-size:32px;line-height:40px;color:var(--white);letter-spacing:-.8px;white-space:nowrap}
.cta-btn{left:729px;top:3034px;width:166px;height:42px;font-size:12px}
.footer-rule{left:243px;top:3115px;width:711px;height:1px;background:#6d73b0}
.footer-note{left:243px;top:3156px;width:711px;text-align:center;font-size:12px;line-height:21px;color:var(--white)}
.field{background:var(--white);border-radius:3px;font-size:10px;color:#555;padding:10px 16px}
.send-btn{left:288px;top:3409px;width:148px;height:34px;border-radius:3px;background:var(--blue);color:var(--white);font-size:10px;display:flex;align-items:center;justify-content:center}
.copyright{left:245px;top:3512px;font-size:10px;font-weight:700;color:#222}
</style>
</head>
<body>

<header class="site-header abs">
  <div class="brand abs"><span class="brand-dot"></span>HARBORLINE PROVISIONS</div>
  <nav class="nav abs"><span>Home</span><span>About Us</span><span>What we do</span><span>Contact Us</span></nav>
  <div class="phone abs">
    <svg width="24" height="24" viewBox="0 0 24 24"><circle cx="12" cy="12" r="11" fill="none" stroke="#0b6fc7" stroke-width="2"/><path d="M8 7l2 0 1 3-1.5 1a7 7 0 0 0 3 3L14 13l3 1v2a1 1 0 0 1-1 1A9 9 0 0 1 7 8a1 1 0 0 1 1-1z" fill="#0b6fc7"/></svg>
    (555) 014-2368
  </div>
</header>

<section>
  <div class="hero-photo abs" role="img" aria-label="Supermarket aisle lined with stocked shelves"></div>
  <div class="hero-circle abs"></div>
  <h1 class="hero-title abs"><span class="accent">Harborline Provisions</span><br>Premier Food and<br>Beverage Broker<br>Company</h1>
  <div class="hero-link abs link-arrow">Contact Us
    <svg width="34" height="10" viewBox="0 0 34 10"><path d="M0 5h32M27 1l5 4-5 4" stroke="#33c6f0" fill="none" stroke-width="1.2"/></svg></div>
</section>

<section>
  <div class="intro-panel abs"></div>
  <h2 class="intro-title abs"><span class="hl">Harborline Provisions</span><br>works with food<br>manufacturers, brand<br>owners, distributors and<br>wholesalers market<br>their products.</h2>
  <div class="intro-btn abs btn-outline link-arrow">Contact Us
    <svg width="34" height="10" viewBox="0 0 34 10"><path d="M0 5h32M27 1l5 4-5 4" stroke="#222" fill="none" stroke-width="1.2"/></svg></div>
  <div class="intro-bar abs"></div>
  <div class="intro-photo abs" role="img" aria-label="Truck with shipping container at a lit warehouse loading dock"></div>
</section>

<section>
  <div class="feature-photo abs" role="img" aria-label="Shopper with a cart in a blurred grocery aisle"></div>

  <div class="card card-service abs">
    <h3>Customer Service</h3>
    <p>Our client relationships are extremely important, and we take the necessary steps to ensure your experience with Harborline Provisions is nothing but the best.</p>
  </div>
  <div class="icon-badge abs" style="left:499px;top:1063px">
    <svg width="44" height="40" viewBox="0 0 44 40" fill="none" stroke="#fff" stroke-width="1.6"><circle cx="18" cy="12" r="7"/><path d="M4 32c1-8 7-12 14-12s10 3 12 7"/><path d="M34 24v10M29 29h10"/></svg>
  </div>

  <div class="card card-quality abs">
    <h3>Quality Guarantee</h3>
    <p>As a trading company, we believe in the food products we buy and what we offer our clients.</p>
  </div>
  <div class="icon-badge abs" style="left:771px;top:1309px">
    <svg width="42" height="40" viewBox="0 0 42 40" fill="none" stroke="#fff" stroke-width="1.6"><path d="M3 5h6l5 20h20l4-14H12"/><circle cx="16" cy="32" r="3"/><circle cx="31" cy="32" r="3"/><path d="M19 15l4 4 6-7"/></svg>
  </div>

  <div class="card card-network abs">
    <h3>Superior Network</h3>
    <p>We source from a large network of relationship, dealing directing with manufacturers to provide our clients with quality surplus products.</p>
  </div>
  <div class="icon-badge abs" style="left:305px;top:1480px">
    <svg width="44" height="44" viewBox="0 0 44 44" fill="none" stroke="#fff" stroke-width="1.6"><circle cx="22" cy="22" r="19"/><ellipse cx="22" cy="22" rx="8" ry="19"/><path d="M3 22h38M6 12h32M6 32h32M22 3v38"/></svg>
  </div>
</section>

<section>
  <div class="services-band abs"></div>
  <p class="eyebrow abs">What we do.</p>
  <h2 class="services-title abs">As experienced food brokers, we aim to push your products to meet and exceed your goals.</h2>
  <div class="services-btn abs btn-outline link-arrow">What we do
    <svg width="44" height="10" viewBox="0 0 44 10"><path d="M0 5h42M37 1l5 4-5 4" stroke="#222" fill="none" stroke-width="1.2"/></svg></div>
  <div class="service-tile tile-sales abs" role="img" aria-label="Team reviewing sales figures at a computer"><span>Sales &amp;<br>Marketing</span></div>
  <div class="service-tile tile-trade abs" role="img" aria-label="Cargo plane over a container yard with a forklift"><span style="left:66px">Trading</span></div>
  <div class="service-tile tile-stock abs" role="img" aria-label="Grocery store aisle stocked with products"><span style="left:40px">Closeout/<br>Excess Inventory</span></div>
</section>

<section>
  <div class="trust-box abs"></div>
  <h2 class="trust-title abs">Trusted by High-Volume, High-Growth Retailers</h2>
  <div class="retailer abs" style="left:282px;top:2614px"></div>
  <div class="retailer abs" style="left:394px;top:2614px"></div>
  <div class="retailer abs" style="left:504px;top:2614px"></div>
  <div class="retailer abs" style="left:614px;top:2614px"></div>
  <div class="retailer abs" style="left:725px;top:2614px"></div>
  <div class="retailer abs" style="left:835px;top:2614px"></div>
  <div class="retailer abs tall" style="left:290px;top:2656px;border-radius:50%;width:60px"></div>
  <div class="retailer abs tall" style="left:394px;top:2656px"></div>
  <div class="retailer abs tall" style="left:504px;top:2656px"></div>
  <div class="retailer abs tall" style="left:622px;top:2656px;width:60px"></div>
  <div class="retailer abs tall" style="left:733px;top:2656px;width:60px;border-radius:50%"></div>
  <div class="retailer abs tall" style="left:843px;top:2656px;width:60px"></div>
</section>

<footer>
  <svg class="footer-wave abs" viewBox="0 0 1200 626" preserveAspectRatio="none">
    <circle cx="612" cy="60" r="72" fill="#0f1766"/>
    <path d="M0 105 Q600 25 1200 55 V626 H0Z" fill="#0f1766"/>
  </svg>
  <div class="footer-brand abs">HARBORLINE PROVISIONS</div>
  <h2 class="cta-title abs">Want to sell your products?</h2>
  <div class="cta-btn abs btn-outline link-arrow">Contact us today
    <svg width="30" height="10" viewBox="0 0 30 10"><path d="M0 5h28M23 1l5 4-5 4" stroke="#222" fill="none" stroke-width="1.2"/></svg></div>
  <div class="footer-rule abs"></div>
  <p class="footer-note abs">Do you have a question or concern? Feel free to call us at 0125550190 or send us a message<br>through the contact form below. We look forward to hearing from you!</p>
  <form>
    <div class="field abs" style="left:290px;top:3228px;width:306px;height:31px">Name</div>
    <div class="field abs" style="left:603px;top:3228px;width:304px;height:31px">Email</div>
    <div class="field abs" style="left:290px;top:3272px;width:306px;height:31px">Phone</div>
    <div class="field abs" style="left:603px;top:3272px;width:304px;height:31px">Subject</div>
    <div class="field abs" style="left:290px;top:3314px;width:617px;height:73px">Message</div>
    <div class="send-btn abs">Send Message</div>
  </form>
  <p class="copyright abs">Copyright 2020 © Harborline Provisions</p>
</footer>

</body>
</html>
```